Redesign Colorful Business Card

Please redesign the card attached. It is too busy. Please don't eliminate any of the words. The repetivite word "free" can be used less often.

Target Market(s)

College Students.

Contact Information for Business Card

The details listed in the attached image

Font styles to use
Sans Serif

Requirements
Must have
• A clear and simple presentation and must be attractive.

```html
<!DOCTYPE html>
<html lang="en">
<head>
<meta charset="UTF-8">
<title>LearnBRYT Business Card</title>
<link rel="stylesheet" href="https://fonts.googleapis.com/css2?family=Anton&family=Montserrat:wght@500;700&family=Open+Sans:wght@400&display=swap">
<style>
  :root {
    --page: #ece9e4;
    --card: #1c1210;
    --yellow: #fff200;
    --red: #e2141f;
    --green: #5cb531;
    --blue: #7ccdf0;
    --white: #ffffff;
    --ray: #efe4a8;
    --accent: #8a4a86;
    --horn-start: #d6202a;
    --horn-end: #f39a12;
  }
  * { margin: 0; padding: 0; box-sizing: border-box; }
  html, body {
    width: 1200px; height: 1200px; overflow: hidden;
    background: var(--page);
  }
  .card {
    position: absolute; left: 100px; top: 314px;
    width: 1000px; height: 572px;
    background: var(--card);
    overflow: hidden;
    box-shadow: 0 6px 18px rgba(0,0,0,.25);
  }
  .card-shapes { position: absolute; inset: 0; }
  .brand-dot {
    position: absolute; left: 115px; top: 120px;
    width: 240px; height: 240px;
    border-radius: 50%;
    background: var(--accent);
  }
  .site-name {
    position: absolute; left: 96px; top: 392px;
    font-family: "Open Sans", sans-serif; font-size: 40px;
    color: var(--white); letter-spacing: .5px;
  }
  .megaphone-art {
    position: absolute; left: 325px; top: 275px;
    width: 80px; height: 50px;
    border-radius: 10px 30px 30px 10px;
    background: linear-gradient(90deg, var(--horn-start), var(--horn-end));
  }
  .free-word {
    position: absolute; left: 425px; top: 238px;
    font-family: "Anton", sans-serif; font-size: 96px; line-height: 1;
    color: var(--yellow);
  }
  .benefit {
    position: absolute;
    font-family: "Montserrat", sans-serif; font-weight: 500;
    font-size: 28px; line-height: 1.25; letter-spacing: .5px;
    text-transform: uppercase;
  }
  .benefit-time { left: 520px; top: 70px; color: var(--yellow); }
  .benefit-class { left: 610px; top: 180px; color: var(--green); }
  .benefit-memory { left: 640px; top: 320px; color: var(--blue); }
  .copyright-band {
    position: absolute; left: 0; top: 478px;
    width: 100%; height: 52px;
    background: var(--red);
    display: flex; align-items: center; padding-left: 58px;
    font-family: "Montserrat", sans-serif; font-weight: 700;
    font-size: 24px; color: var(--white);
  }
</style>
</head>
<body>
  <div class="card">
    <svg class="card-shapes" width="1000" height="572" viewBox="0 0 1000 572" aria-hidden="true">
      <polygon points="0,0 250,0 0,250" fill="var(--yellow)"/>
      <polygon points="1000,330 1000,572 760,572" fill="var(--yellow)"/>
      <g stroke="var(--ray)" stroke-width="2">
        <line x1="392" y1="262" x2="432" y2="172"/>
        <line x1="402" y1="266" x2="470" y2="196"/>
        <line x1="410" y1="272" x2="492" y2="226"/>
        <line x1="412" y1="340" x2="505" y2="372"/>
        <line x1="405" y1="346" x2="478" y2="398"/>
        <line x1="396" y1="350" x2="444" y2="418"/>
      </g>
    </svg>

    <div class="brand-dot" aria-hidden="true"></div>
    <div class="site-name">LearnBRYT.com</div>

    <div class="megaphone-art" role="img" aria-label="Megaphone illustration"></div>
    <div class="free-word">FREE</div>

    <p class="benefit benefit-time">Cut study time<br>down by up to 50 %</p>
    <p class="benefit benefit-class">Learn a subject<br>without having to<br>go to class</p>
    <p class="benefit benefit-memory">Memorize<br>anything<br>quickly</p>

    <div class="copyright-band">Copyright BRYT services, LLC 2013-2022 All rights reserved</div>
  </div>
</body>
</html>
```